Etiketten für Gin
Zielgruppe
Wir vertreiben einen regionalen Gin mit Fichtennadeln.
Zielgruppe sind Gin-Trinker, Wanderer, Besucher und Bewohner der Bergischen Landes.
Aufgabenstellung
Benötigt wird ein zweiteiliges Etikett für eine 500 ml Flasche (Höhe 320 mm, Durchmesser ca. 75 mm). Datenblatt in der Anlage. Die Flasche wird einen schwarzen Stopfen bekommen,
Das vordere Etikett soll eine Größe von 80 mm (Breite) x 160 mm (Höhe) haben. Das Etikett für die Rückseite soll eine Größe von 60 mm (Breite) x 100 mm (Höhe) haben.
Aufgrund des schwarzen Stopfens wird ein Etikett mit/in schwarz favorisiert. Auf der Vorderseite soll unser Logo (bei den Dateien) abgebildet sein.
Pflichtangaben Vorderseite: auf dem vorderen Etikett müssen die Pflichtangaben zur Nettofüllmenge und zum Alkoholgehalt angegeben sein. Sprich, auf der Vorderseite muss 500 ml und 43 % untergebracht sein. Diese Pflichtangaben müssen zwingend eine Höhe von 4 mm haben (gesetzlich vorgeschrieben). Gleiches gilt für die Verkehrsbezeichnung Gin, die im Logo enthalten ist. Das Wort Gin muss ebenfalls eine Größe von mindestens 4 mm haben.
Auf dem rückwärtigen Etikett müssen folgende Pflichtangaben vorhanden sein:
Talwerk Brand
Lukas Dornfeld
Anton-Weller-Straße 27
51467 Bergisch Gladbach
Des Weiteren wären auf der Rückseite zwei Felder wünschenswert, in die man zum einen die Batch No. und zum anderen die Flaschennummer eintragen kann (Beispiel Bild 'Batch_Flasche'). Zudem ein weißes Feld, in dem später der EAN Code Ei gepflegt werden kann.
Als Text für die Rückseite:
Wo Natur auf Geschmack trifft
Das 'Bergische Gefühl' erleben Sie mit dem Talwerk Brand Gin. Lassen Sie einen naturverbundenen Tag zum Ausklang, beispielsweise nach einer Wanderung, noch einmal an Ihnen vorbeiziehen.
Erinnern Sie sich durch die bei der Herstellung geschmacksgebenden Botanicals von der Fichte an einen erholsamen Spaziergang durch die Wälder des Bergischen Landes.
Mehr Informationen unter
www.talwerk-brand.de
Druckdatenanlieferung laut Druckerei:
Dateiform..

```html
<!DOCTYPE html>
<html lang="de">
<head>
<meta charset="utf-8">
<title>Talwerk Brand Gin – Etiketten</title>
<link rel="stylesheet" href="https://fonts.googleapis.com/css2?family=Josefin+Sans:wght@300;400&family=Oswald:wght@400&family=Roboto:wght@400&display=swap">
<style>
  :root {
    --page: #ffffff;
    --label-black: #1b1c1b;
    --band-dark: #27331f;
    --band-line: #3d5a26;
    --forest-light: #cfe39a;
    --forest-mid: #8cc63f;
    --forest-deep: #4d8a22;
    --moss-top: #2f4a22;
    --moss-bottom: #1f3317;
    --accent: #7fbf3a;
    --text-light: #f4f4f0;
    --table-line: #c9c9c4;
  }
  * { margin: 0; padding: 0; box-sizing: border-box; }
  html, body { width: 1200px; height: 800px; overflow: hidden; background: var(--page); }
  .sheet {
    width: 1200px; height: 800px;
    display: flex; align-items: center; justify-content: center; gap: 40px;
  }
  .label {
    position: relative; height: 562px; background: var(--label-black);
    box-shadow: 0 4px 10px rgba(0,0,0,.25); overflow: hidden; color: var(--text-light);
  }
  .label--front { width: 500px; }
  .label--back { width: 422px; }
  .forest-band {
    position: absolute; left: 0; top: 0; width: 100%; height: 80px;
    background: linear-gradient(180deg, var(--forest-light) 0%, var(--forest-mid) 45%, var(--forest-deep) 100%);
  }
  .band-rule {
    position: absolute; left: 0; width: 100%; height: 12px;
    background: var(--band-dark); border-top: 2px solid var(--band-line); border-bottom: 2px solid var(--band-line);
  }
  .band-rule--top { top: 80px; }
  .band-rule--bottom { top: 468px; }
  .moss-band {
    position: absolute; left: 0; bottom: 0; width: 100%; height: 82px;
    background: linear-gradient(180deg, var(--moss-top), var(--moss-bottom));
  }
  /* front */
  .brand-mark {
    position: absolute; left: 50%; top: 140px; width: 120px; height: 120px;
    margin-left: -60px; border-radius: 50%; background: var(--accent);
  }
  .brand-name {
    position: absolute; left: 0; top: 346px; width: 100%; text-align: center;
    font-family: "Josefin Sans", sans-serif; font-weight: 300; font-size: 52px;
    letter-spacing: 2px; text-transform: uppercase; color: var(--text-light);
  }
  .front-facts {
    position: absolute; left: 42px; right: 42px; top: 418px;
    display: flex; justify-content: space-between; align-items: baseline;
    font-family: "Oswald", sans-serif; font-size: 23px;
  }
  .front-facts .gin { color: var(--accent); letter-spacing: 8px; font-family: "Josefin Sans", sans-serif; }
  /* back */
  .back-content {
    position: absolute; left: 50px; right: 50px; top: 112px; text-align: center;
  }
  .back-title {
    font-family: "Oswald", sans-serif; font-weight: 400; font-size: 25px;
    color: var(--accent); text-transform: uppercase; letter-spacing: -.3px; margin-bottom: 10px;
  }
  .back-text {
    font-family: "Roboto", sans-serif; font-size: 11.5px; line-height: 17.5px;
    text-align: justify; text-align-last: center; margin-bottom: 6px;
  }
  .more-info {
    font-family: "Oswald", sans-serif; font-size: 17px; color: var(--accent);
    text-transform: uppercase; margin-top: 6px;
  }
  .website { font-family: "Roboto", sans-serif; font-size: 12px; margin-top: 2px; }
  .batch-table {
    position: absolute; left: 50px; top: 368px; width: 310px;
    border-collapse: collapse; font-family: "Roboto", sans-serif; font-size: 10.5px; text-align: center;
  }
  .batch-table td, .batch-table th { border: 1px solid var(--table-line); height: 33px; }
  .batch-table th {
    font-family: "Oswald", sans-serif; font-weight: 400; font-size: 13px; color: var(--accent);
  }
  .batch-table .producer { width: 155px; line-height: 11px; vertical-align: top; padding-top: 4px; }
  .batch-table .producer span { display: block; font-family: "Oswald", sans-serif; color: var(--accent); font-size: 12px; line-height: 14px; text-transform: uppercase; }
</style>
</head>
<body>
<main class="sheet">
  <section class="label label--front">
    <div class="forest-band" role="img" aria-label="Illustrierte Silhouette eines Fichtenwaldes in Grüntönen"></div>
    <div class="band-rule band-rule--top"></div>
    <div class="brand-mark"></div>
    <h1 class="brand-name">Talwerk Brand</h1>
    <div class="front-facts">
      <span class="volume">500ML</span>
      <span class="gin">• GIN •</span>
      <span class="abv">43% VOL</span>
    </div>
    <div class="band-rule band-rule--bottom"></div>
    <div class="moss-band" role="img" aria-label="Moosgrüne Waldbodentextur"></div>
  </section>

  <section class="label label--back">
    <div class="forest-band" role="img" aria-label="Illustrierte Silhouette eines Fichtenwaldes in Grüntönen"></div>
    <div class="band-rule band-rule--top"></div>
    <div class="back-content">
      <h2 class="back-title">Wo Natur auf Geschmack trifft</h2>
      <p class="back-text">Das 'Bergische Gefühl' erleben Sie mit dem Talwerk Brand Gin. Lassen Sie einen naturverbundenen Tag zum Ausklang, beispielsweise nach einer Wanderung, noch einmal an Ihnen vorbeiziehen.</p>
      <p class="back-text">Erinnern Sie sich durch die bei der Herstellung geschmacksgebenden Botanicals von der Fichte an einen erholsamen Spaziergang durch die Wälder des Bergischen Landes.</p>
      <p class="more-info">• Mehr Informationen unter •</p>
      <p class="website">www.talwerk-brand.de</p>
    </div>
    <table class="batch-table">
      <tr>
        <td class="producer" rowspan="2"><span>Talwerk Brand</span>Lukas Dornfeld<br>Anton-Weller-Straße 27<br>51467 Bergisch Gladbach</td>
        <th>BATCH NR.</th>
        <th>BOTTLE NR.</th>
      </tr>
      <tr>
        <td>L123/2022</td>
        <td>12345</td>
      </tr>
    </table>
    <div class="band-rule band-rule--bottom"></div>
    <div class="moss-band" role="img" aria-label="Moosgrüne Waldbodentextur"></div>
  </section>
</main>
</body>
</html>
```